Banner ad for hyper local news site

We need a banner (that we will use on our own site) to explain to people that they can "be the reporter" in their local area. Lanternway is an Australia community news network. We cover local news on a daily basis but also allow people and organisations to publish their own news direct to the site. We are trying to encourage local dialogue and to empower people to talk about the things that matter to them and get their issues on the news agenda.

We need a 'call to action' banner that explains to our users that they can post their own stories on the site.

Some suggested text (thinking this would be rolling)

*Lanternway is YOUR voice in the community
*You can 'be the reporter' and write your own news
*To be heard, contribute your stories, click here - it's free

The banner doesn't have to be slick - we'd prefer a warm and friendly community feeling....but also something in keeping with the look and feel of our site wwww.lanternway-example.com.au

Industry/Entity Type

News

```html
<!DOCTYPE html>
<html lang="en">
<head>
<meta charset="utf-8">
<title>Lanternway banner – rolling frames</title>
<link rel="stylesheet" href="https://fonts.googleapis.com/css2?family=Arimo:wght@400;700&display=swap">
<style>
  :root {
    --page-bg: #ffffff;
    --ink: #111111;
    --frame-border: #2a2a2a;
    --green-light: #5cd24e;
    --green-mid: #2fae2a;
    --green-dark: #17801a;
    --green-edge: #0f6a12;
    --text-light: #ffffff;
    --cta-yellow: #ffe600;
    --photo-a: #cfd8df;
    --photo-b: #7a8a98;
    --photo-c: #e9d3b4;
  }
  * { box-sizing: border-box; margin: 0; padding: 0; }
  html, body {
    width: 1200px;
    height: 614px;
    overflow: hidden;
    background: var(--page-bg);
    font-family: "Arimo", Arial, sans-serif;
  }
  .storyboard {
    position: relative;
    width: 1200px;
    height: 614px;
  }
  .frame-row {
    position: absolute;
    left: 0;
    width: 1200px;
    height: 105px;
  }
  .frame-row--1 { top: 99px; }
  .frame-row--2 { top: 245px; }
  .frame-row--3 { top: 394px; }

  .frame-label {
    position: absolute;
    left: 76px;
    top: 0;
    height: 105px;
    line-height: 105px;
    font-size: 29px;
    color: var(--ink);
  }
  .banner {
    position: absolute;
    left: 239px;
    top: 0;
    width: 831px;
    height: 105px;
    border: 2px solid var(--frame-border);
    background: var(--page-bg);
    overflow: hidden;
  }
  .banner__pill {
    position: absolute;
    left: 7px;
    top: 7px;
    width: 600px;
    height: 89px;
    border-radius: 16px;
    border: 1px solid var(--green-edge);
    background:
      repeating-linear-gradient(0deg, rgba(255,255,255,0.05) 0 2px, rgba(0,0,0,0.04) 2px 4px),
      linear-gradient(180deg, var(--green-light) 0%, var(--green-mid) 45%, var(--green-dark) 100%);
    box-shadow: inset 0 2px 3px rgba(255,255,255,0.35);
  }
  .banner__message {
    position: absolute;
    left: 7px;
    top: 7px;
    width: 560px;
    height: 89px;
    display: flex;
    flex-direction: column;
    justify-content: center;
    align-items: center;
    text-align: center;
    color: var(--text-light);
    font-size: 28px;
    line-height: 1.15;
    text-shadow: 0 1px 2px rgba(0,0,0,0.35);
  }
  .banner__cta {
    color: var(--cta-yellow);
    font-weight: 700;
    text-shadow: 0 2px 2px rgba(0,0,0,0.55);
  }
  .banner__visual {
    position: absolute;
    right: 0;
    top: 0;
    width: 262px;
    height: 101px;
    background: linear-gradient(90deg, var(--photo-b) 0%, var(--photo-a) 55%, var(--photo-c) 100%);
  }
</style>
</head>
<body>
<main class="storyboard">
  <section class="frame-row frame-row--1">
    <span class="frame-label">Frame 1</span>
    <div class="banner">
      <div class="banner__pill"></div>
      <div class="banner__visual" role="img" aria-label="Laptop showing the Lanternway news site beside a smiling community reporter"></div>
      <p class="banner__message">
        <span>Lanternway is YOUR voice</span>
        <span>in the community</span>
      </p>
    </div>
  </section>

  <section class="frame-row frame-row--2">
    <span class="frame-label">Frame 2</span>
    <div class="banner">
      <div class="banner__pill"></div>
      <div class="banner__visual" role="img" aria-label="Laptop showing the Lanternway news site beside a smiling community reporter"></div>
      <p class="banner__message">
        <span>You can 'be the reporter'</span>
        <span>and write your own news</span>
      </p>
    </div>
  </section>

  <section class="frame-row frame-row--3">
    <span class="frame-label">Frame 3</span>
    <div class="banner">
      <div class="banner__pill"></div>
      <div class="banner__visual" role="img" aria-label="Laptop showing the Lanternway news site beside a smiling community reporter"></div>
      <p class="banner__message">
        <span>To be heard, contribute your stories,</span>
        <span class="banner__cta">click here - it's free</span>
      </p>
    </div>
  </section>
</main>
</body>
</html>
```